CoinLantern one-page corporate website

Our company, CoinLantern is a cryptocurrency Initial Coin Offering ("ICO" marketing and promotion agency, which requires a professional company landing page design whereby prospective clients can learn;
-who we are
-what we do
-what our people are saying about us
-core team members
-subscribe to our mailing list
-how to get in touch (basic contact form)

We are looking for something unique and attractive -- not a standard Vanto template that we could put together ourselves. Plain stock images should not be used. Unique visualizations of the service offerings and creative presentation are key. We are a cutting edge marketing agency and as such, we need to look the part.

Relevant documentation about the business and branding assets have been attached to guide the designer. Certain information will be included by the company at a later date such as team member descriptions. As such, lorem ipsum may be included wherever necessary to help visualize the textual areas.

****Please ensure that you actually utilize the photos and graphics provided so that we can have a good picture of what it would actually look like with our branding.

The site must be responsive HTML CSS Design.

Sites style themes we like for inspiration and specific sections we like ****Very important***:
https://fundrivermesh.com/offers - we like that the token & company logo is used in unique visualizations that connects various ideas together. We imagine unique visuals such as these with our Icon (see attached) serving as a token. We also like the unique and attractive visual theme of the webpage itself.

https://pavoniaholdings.com/ - we like the layout of this website, specifically how the service offerings are displayed in a circular visual graphic with the Pavonia logo in the middle. We imagine a similar type of graphic designed with CoinLantern in the middle.

https://quorvanet.org/ - we like how the logo is central to the theme in this site when you first enter and how it fades + shrinks into the distance as you scroll down.

Target Market(s)

cryptocurrency entrepreneurs and ICOs

Industry/Entity Type

It Company

Coding

Coded - Design and coding required

Number of Pages Required

1 page

Font styles to use
Sans Serif

Colors

Designer to choose colors to be used in the design.

Requirements
Must have
• The site must be responsive HTML CSS Design.
• The page must be modern and visually attractive. Elements must not be static and should have a fluid motion / visual change as the user scrolls through the page.
Should not have
• The project should not use any old stock images or elements which are dull and over-used, but rather images or elements should be unique and well thought out.

```html
<!DOCTYPE html>
<html lang="en">
<head>
<meta charset="utf-8">
<title>CoinLantern – Newsletter & Contact</title>
<link href="https://fonts.googleapis.com/css2?family=Poppins:wght@400;500&family=Open+Sans:wght@400;600&family=Roboto:wght@400&display=swap" rel="stylesheet">
<style>
:root{
  --navy:#1d4570;
  --navy-deep:#1b4269;
  --sky:#19a3e6;
  --ink:#333;
  --line:#a9a9a9;
  --placeholder:#777;
  --footer-bg:#2f3031;
  --footer-bg-2:#3a3b3c;
  --white:#fff;
}
*{margin:0;padding:0;box-sizing:border-box}
html,body{width:1200px;height:946px;overflow:hidden}
body{position:relative;font-family:"Open Sans",sans-serif;color:var(--ink);background:var(--white)}
.abs{position:absolute}

/* newsletter */
.newsletter{left:0;top:0;width:1200px;height:216px;background:var(--navy);color:var(--white);text-align:center}
.newsletter h2{position:absolute;left:0;right:0;top:25px;font:400 36px/1 "Poppins",sans-serif;letter-spacing:-.3px}
.newsletter p{position:absolute;left:0;right:0;top:69px;font-size:12px}
.signup{position:absolute;left:431px;top:129px;width:337px;height:37px;display:flex;border:1px solid var(--white)}
.signup .field{flex:1;background:var(--white);color:#333;font-size:13px;text-align:left;padding:9px 12px}
.signup .btn{width:107px;background:var(--sky);color:var(--white);font-size:12px;line-height:35px}

/* contact */
.contact h2{position:absolute;left:0;right:0;top:258px;text-align:center;font:400 36px/1 "Poppins",sans-serif;color:var(--navy)}
.contact .lead{position:absolute;left:0;right:0;top:300px;text-align:center;font-size:12px}
.input{position:absolute;border:1px solid var(--line);display:flex;background:var(--white)}
.input .ico{width:33px;border-right:1px solid var(--line);display:flex;align-items:center;justify-content:center}
.input .label{padding-left:9px;font:400 11.5px "Roboto",sans-serif;color:var(--placeholder);display:flex;align-items:center;letter-spacing:.2px}
.input.tall .ico,.input.tall .label{align-items:flex-start;padding-top:28px}
.send{position:absolute;left:503px;top:543px;width:194px;height:39px;border:2px solid var(--navy);border-radius:20px;display:flex;align-items:center;justify-content:center;gap:5px;font:400 14px "Roboto",sans-serif;color:var(--navy)}

/* footer */
.footer{left:0;top:641px;width:1200px;height:305px;background:linear-gradient(135deg,var(--footer-bg-2),var(--footer-bg) 60%,#2a2b2c)}
.info-bar{left:132px;top:641px;width:936px;height:67px;background:var(--navy-deep);color:var(--white)}
.social{position:absolute;top:19px;width:28px;height:28px;border:2px solid var(--white);border-radius:50%;display:flex;align-items:center;justify-content:center}
.info-bar .item{position:absolute;top:14px;font-size:13.5px;line-height:18px;display:flex;gap:8px}
.info-bar .item svg{margin-top:8px;flex:none}
.brand{left:132px;top:732px;display:flex;align-items:center;gap:8px;color:var(--white)}
.brand .mark{width:44px;height:44px;border:2px solid var(--white);border-radius:50%}
.brand .name{font:400 27px "Poppins",sans-serif}
.tagline{left:242px;top:766px;font-size:10px;color:#ccc}
.about{left:133px;top:798px;width:250px;font-size:12px;line-height:22px;color:var(--white)}
.col-title{font:500 18px "Poppins",sans-serif;color:var(--white);letter-spacing:.3px}
.col-title::after{content:"";display:block;width:56px;height:2px;background:var(--sky);margin:2px 0 0 2px}
.links{list-style:none;margin-top:18px}
.links li{font-size:11.5px;line-height:18.6px;color:var(--white);letter-spacing:.2px}
.hours{left:852px;top:731px;width:216px;color:var(--white);font:500 13.4px "Poppins",sans-serif;letter-spacing:-.2px;white-space:nowrap}
.hours .row{height:52px;border-bottom:1px solid #888;padding-top:2px}
.hours .row:last-child{border:0;padding-top:14px}
.hours .row:nth-child(2){padding-top:18px}
.closed{color:var(--sky);margin-left:10px}
.rule{left:0;top:892px;width:1200px;height:1px;background:#666}
.copy{left:0;right:0;top:909px;text-align:center;color:var(--white);font-size:13.5px}
.top-btn{left:1039px;top:905px;width:28px;height:27px;background:var(--navy-deep);display:flex;align-items:center;justify-content:center}
</style>
</head>
<body>

<section class="abs newsletter">
  <h2>JOIN OUR NEWSLETTER</h2>
  <p>Sign up for our newsletter</p>
  <div class="signup"><div class="field">Enter your email address</div><div class="btn">SUBSCRIBE</div></div>
</section>

<section class="contact">
  <h2>KEEP IN TOUCH</h2>
  <p class="lead">Curabitur eget iaculis turpis. Donec varius consectetur</p>

  <div class="input" style="left:291px;top:349px;width:298px;height:33px">
    <div class="ico"><svg width="12" height="13" viewBox="0 0 12 13" fill="none" stroke="#888"><circle cx="6" cy="4" r="3"/><path d="M1 12.5c0-3 2-4.5 5-4.5s5 1.5 5 4.5z"/></svg></div>
    <div class="label">NAME</div>
  </div>
  <div class="input" style="left:612px;top:349px;width:298px;height:33px">
    <div class="ico"><svg width="9" height="14" viewBox="0 0 9 14" fill="none" stroke="#888"><rect x=".5" y=".5" width="8" height="13" rx="1"/><path d="M.5 10.5h8"/></svg></div>
    <div class="label">PHONE</div>
  </div>
  <div class="input" style="left:291px;top:400px;width:298px;height:34px">
    <div class="ico"><svg width="13" height="10" viewBox="0 0 13 10" fill="none" stroke="#888"><rect x=".5" y=".5" width="12" height="9"/><path d="M.5 .5l6 5 6-5"/></svg></div>
    <div class="label">EMAIL</div>
  </div>
  <div class="input" style="left:612px;top:400px;width:298px;height:34px">
    <div class="ico"><svg width="11" height="13" viewBox="0 0 11 13" fill="none" stroke="#888"><path d="M.5.5h7l3 3v9h-10z M3 6h5M3 8h5M3 10h5"/></svg></div>
    <div class="label">SUBJECT</div>
  </div>
  <div class="input tall" style="left:291px;top:450px;width:619px;height:68px">
    <div class="ico"><svg width="13" height="10" viewBox="0 0 13 10" fill="none" stroke="#888"><rect x=".5" y=".5" width="12" height="9"/><path d="M.5 .5l6 5 6-5"/></svg></div>
    <div class="label" style="padding-top:28px">MESSAGE</div>
  </div>

  <div class="send">SEND MESSAGE
    <svg width="14" height="13" viewBox="0 0 14 13" fill="none" stroke="#1d4570" stroke-width="1.4"><path d="M13 1L1 6l4 1.5L13 1 7 9.5V12l2-2.5 2 1.5z"/></svg>
  </div>
</section>

<footer>
  <div class="abs footer" role="img" aria-label="Muted grey street map of the surrounding region"></div>

  <div class="abs info-bar">
    <span class="social" style="left:51px" aria-label="Share"><svg width="12" height="12" viewBox="0 0 12 12" fill="#fff"><circle cx="2.5" cy="6" r="2"/><circle cx="9.5" cy="2.5" r="2"/><circle cx="9.5" cy="9.5" r="2"/><path d="M2.5 6L9.5 2.5M2.5 6l7 3.5" stroke="#fff" stroke-width="1.2"/></svg></span>
    <span class="social" style="left:87px" aria-label="Message"><svg width="12" height="11" viewBox="0 0 12 11" fill="#fff"><path d="M1 0h10a1 1 0 0 1 1 1v6a1 1 0 0 1-1 1H5l-3 3V8H1a1 1 0 0 1-1-1V1a1 1 0 0 1 1-1z"/></svg></span>
    <span class="social" style="left:124px" aria-label="Follow"><svg width="11" height="11" viewBox="0 0 11 11" fill="none" stroke="#fff" stroke-width="2"><path d="M5.5 0v11M0 5.5h11"/></svg></span>
    <div class="item" style="left:240px">
      <svg width="12" height="17" viewBox="0 0 12 17"><path d="M6 0a6 6 0 0 1 6 6c0 4-6 11-6 11S0 10 0 6a6 6 0 0 1 6-6z" fill="#fff"/><circle cx="6" cy="6" r="2.2" fill="#1b4269"/></svg>
      <span>1842 Harlow Crest Avenue<br>Brenfield, NY 11907</span></div>
    <div class="item" style="left:479px">
      <svg width="16" height="16" viewBox="0 0 16 16"><path d="M3 0l3 3.5-2 2c1 2.5 3.5 5 6 6l2-2L16 13l-2.5 3C6 15 1 10 0 2.5z" fill="#fff"/></svg>
      <span>(01) 47 - 310 582 64<br>(01) 47 - 310 927 15</span></div>
    <div class="item" style="left:718px">
      <svg width="17" height="13" viewBox="0 0 17 13"><rect width="17" height="13" rx="1" fill="#fff"/><path d="M0 1l8.5 6L17 1" fill="none" stroke="#1b4269" stroke-width="1.4"/></svg>
      <span>admin@lanternpost.com<br>info@lanternpost.com</span></div>
  </div>

  <div class="abs brand"><span class="mark"></span><span class="name">CoinLantern</span></div>
  <div class="abs tagline">The Token Sale Experts</div>
  <p class="abs about">Lorem ipsum dolor sit amet, consectetur adipiscing elit. Suspendisse dictum varius metusnec convallis leo egestas et.</p>

  <div class="abs" style="left:450px;top:731px">
    <h3 class="col-title">USEFUL LINKS</h3>
    <ul class="links"><li>BROWSE INVESTMENTS</li><li>TERMS&nbsp; AND&nbsp; CONDITIONS</li><li>PRIVACY</li><li>APPLY FOR FINANCE</li><li>RISK&nbsp; WARNINGS</li></ul>
  </div>
  <div class="abs" style="left:667px;top:731px">
    <h3 class="col-title">USEFUL LINKS</h3>
    <ul class="links"><li>ADVANTAGE</li><li>PARTNERS</li><li>CAREERS</li><li>SUPPORT</li><li>BLOG</li></ul>
  </div>

  <div class="abs hours">
    <div class="row">Mon - Friday&nbsp; 10:00am - 06:00pm</div>
    <div class="row">Saturday 10:00am - 02:00pm</div>
    <div class="row">Sunday<span class="closed">CLOSED</span></div>
  </div>

  <div class="abs rule"></div>
  <p class="abs copy">CoinLantern © Copyrights 2017</p>
  <div class="abs top-btn"><svg width="8" height="8" viewBox="0 0 8 8" fill="none" stroke="#fff" stroke-width="1.4"><path d="M1 4l3-3 3 3M1 7.5l3-3 3 3"/></svg></div>
</footer>

</body>
</html>
```